Need somewhat upscale, eye catching honey jar label to make our product stand out on store shelves.

We need front and back labels for a honey jar. Files "Honey Jar Front Label 2" & "Honey Jar Back Label 2" show what I have come up with.

Files "Honey Jar Front Label 2". I did this as an example. It shows the information that needs to be included on the front label. The picture was taken by my daughter. The information and picture can be rearranged, enlarged, reduced, cropped, etc. as you see fit.

Files "Honey Jar Back Label 2". I did this one to play with the wording to get the information to fit. It explains how I keep bees. It can be worded differently as long as all the information is included.

I know nothing about good use of color, borders, backgrounds, font style and size, etc. so please excuse my plain presentations. I admire and respect your creative abilities very much.

Since my method of keeping bees involves a lot of travel time and expense, as mentioned in files "Honey Jar Back Label 2" I will try to price my honey a little higher than the competition so please design accordingly with that in mind.

We think we want to use a traditional jar with stick on labels like Marlow's jar seen in file Marlow's Jar. However, feel free to use a different jar as long as the honey can be easily scooped out with a spoon and does not have to be poured out. I know that eliminates a lot of fancy jars but that's what my customers want. Jar size should be 12 ounces which will hold a little more than 1 pound of honey.

Hanging labels are also acceptable therefore jar shapes that will not accept a stick on label can also be used. An example is a Honeypot Jar.

And of course we like Hexagon Jars which are 6 sided like the cells in honeycomb.

Please stick to glass jars that are readily available. No custom shaped jars for now.

Marlow's jar is clear glass and the metal lid is a light golden color.

It's probably a good idea for the shape of the labels to match the shape of the bottle like I marked in black on Marlow's Jar. Being wider in the middle should allow the back label to be shorter than my example seen in files "Honey Jar Back Label 2". I think front and back labels should be the same size.

The shape of the area marked in black around Marlow's label measures 1-1/4 (1.25) inches across the top, 2-1/4 (2.25) inches across the middle, 2 inches across the bottom and 3-1/2 (3.5) inches tall from top to bottom.

Target Market(s)

People wanting local honey that is not processed in any way.
People that are willing to pay a little more for honey from bees that are kept in a sustainable way (see the story in files 2 & 17) without the use of harsh chemicals.

Industry/Entity Type

Travel

Font styles to use
Serif
Decorative
Script

Requirements
Must have
• See my lengthy project description, file "Honey Jar Front Label 2" and file "Honey Jar Back Label 2". All of the info. therein is very important.
• Somewhat upscale, eye catching appearance that makes the product stand out on store shelves and suggests that the honey inside is quality, unprocessed truly local honey.
Nice to have
• If bullets are used they can look like a skep (type of beehive). I have included an example in a file.
• Swirly dashed line coming off the s in lin-Wren's with a honeybee at the end of it. See files for examples.
• Swirly dashed line coming off the i in wildflower making the shape of a heart with a honeybee at the end of it hovering over the o in wildflower and the o looks like a flower. See files for examples.

```html
<!DOCTYPE html>
<html lang="en">
<head>
<meta charset="utf-8">
<title>lin-Wren's Local Honey – Jar Labels</title>
<link rel="stylesheet" href="https://fonts.googleapis.com/css2?family=Cinzel:wght@400;600&family=Tenor+Sans&display=swap">
<style>
  :root {
    --backdrop: #ebe8e3;
    --label-black: #1b1b1b;
    --gold: #c9a227;
    --gold-deep: #a8841a;
    --text-light: #dcdcdc;
    --text-muted: #bdbdbd;
  }
  * { margin: 0; padding: 0; box-sizing: border-box; }
  html, body {
    width: 1200px; height: 768px; overflow: hidden;
    background: var(--backdrop);
  }
  .canvas { position: relative; width: 1200px; height: 768px; }

  .label {
    position: absolute; top: 96px;
    width: 440px; height: 600px;
    font-family: "Tenor Sans", sans-serif;
    color: var(--text-light);
    text-align: center;
  }
  .label--front { left: 140px; }
  .label--back  { left: 620px; }
  .label-shape { position: absolute; inset: 0; width: 100%; height: 100%; }
  .label-content { position: absolute; inset: 0; }

  /* Front */
  .stars { position: absolute; top: 52px; width: 100%; color: var(--gold); font-size: 13px; letter-spacing: 4px; }
  .premium { position: absolute; top: 70px; width: 100%; font-family: "Cinzel", serif; font-size: 34px; color: var(--gold); letter-spacing: 2px; }
  .brand-name { position: absolute; top: 118px; width: 100%; font-size: 40px; color: var(--gold); }
  .product-badge {
    position: absolute; top: 178px; left: 72px; width: 296px; height: 66px;
    border: 3px solid var(--gold); border-radius: 16px;
    background: linear-gradient(#3a3a3a, #202020);
    font-size: 40px; line-height: 58px; color: var(--text-light);
  }
  .claims { position: absolute; top: 262px; width: 100%; font-size: 20px; line-height: 25px; color: var(--text-muted); }
  .tagline { position: absolute; top: 346px; width: 100%; font-size: 25px; color: var(--gold); }
  .bee-trail {
    position: absolute; top: 384px; left: 170px; width: 170px; height: 66px;
    border-radius: 33px;
    background: radial-gradient(ellipse at 75% 40%, rgba(201,162,39,0.45), rgba(27,27,27,0) 70%);
  }
  .variety { position: absolute; top: 456px; width: 100%; font-size: 40px; color: var(--text-light); }
  .net-weight { position: absolute; top: 506px; width: 100%; font-size: 18px; color: var(--text-muted); }
  .comb {
    position: absolute;
    background: linear-gradient(135deg, var(--gold), var(--gold-deep));
    opacity: 0.85; border-radius: 8px;
  }
  .comb--left  { left: 96px;  top: 540px; width: 112px; height: 38px; }
  .comb--right { left: 342px; top: 446px; width: 52px;  height: 96px; }

  /* Back */
  .origin { position: absolute; top: 36px; width: 100%; font-size: 19px; line-height: 22px; }
  .origin-counties { position: absolute; top: 82px; left: 80px; width: 280px; font-size: 14px; line-height: 17px; color: var(--text-muted); }
  .section-title { position: absolute; top: 136px; width: 100%; font-size: 20px; font-weight: 400; }
  .story { position: absolute; top: 166px; left: 55px; width: 330px; font-size: 11px; line-height: 13.5px; color: var(--text-muted); }
  .story p { margin-bottom: 3px; }
  .web { position: absolute; top: 366px; width: 100%; font-size: 12px; }
  .nutrition { position: absolute; top: 386px; left: 60px; width: 320px; font-size: 12px; line-height: 14px; color: var(--text-muted); }
  .nutrition-title { font-size: 16px; line-height: 20px; color: var(--text-light); }
  .nutrition table { margin: 4px auto 0; border-collapse: collapse; text-align: left; font-size: 12px; }
  .nutrition td { padding: 0 10px; line-height: 14px; }
  .bee-mark {
    position: absolute; top: 456px; left: 340px; width: 44px; height: 40px; border-radius: 50%;
    background: radial-gradient(circle, rgba(201,162,39,0.8), rgba(220,220,220,0.25) 70%);
  }
</style>
</head>
<body>
<main class="canvas">

  <section class="label label--front">
    <svg class="label-shape" viewBox="0 0 440 600" aria-hidden="true">
      <defs>
        <linearGradient id="sheen-front" x1="0" y1="0" x2="1" y2="1">
          <stop offset="0" stop-color="#2c2c2c"/>
          <stop offset="0.5" stop-color="#1b1b1b"/>
          <stop offset="1" stop-color="#141414"/>
        </linearGradient>
      </defs>
      <path d="M120,20 Q220,2 320,20 C420,120 440,300 420,420 C410,500 392,556 362,582 Q220,602 78,582 C48,556 30,500 20,420 C0,300 20,120 120,20 Z"
            fill="url(#sheen-front)" stroke="#c9a227" stroke-width="5"/>
    </svg>
    <div class="label-content">
      <div class="stars">★★★★★</div>
      <div class="premium">PREMIUM</div>
      <div class="brand-name">lin-Wren's</div>
      <div class="product-badge">Local Honey</div>
      <div class="claims">100% Pure, Raw, Unaltered<br>Never Heated<br>Strained Not Micro-filtered</div>
      <div class="tagline">She works hard for the honey</div>
      <div class="bee-trail" role="img" aria-label="Honeybee at the end of a dashed heart-shaped flight trail"></div>
      <div class="variety">Wildflower</div>
      <div class="net-weight">Net Weight 16 oz /454g</div>
      <div class="comb comb--left" role="img" aria-label="Gold honeycomb cells"></div>
      <div class="comb comb--right" role="img" aria-label="Gold honeycomb cells"></div>
    </div>
  </section>

  <section class="label label--back">
    <svg class="label-shape" viewBox="0 0 440 600" aria-hidden="true">
      <defs>
        <linearGradient id="sheen-back" x1="0" y1="0" x2="1" y2="1">
          <stop offset="0" stop-color="#2c2c2c"/>
          <stop offset="0.5" stop-color="#1b1b1b"/>
          <stop offset="1" stop-color="#141414"/>
        </linearGradient>
      </defs>
      <path d="M120,20 Q220,2 320,20 C420,120 440,300 420,420 C410,500 392,556 362,582 Q220,602 78,582 C48,556 30,500 20,420 C0,300 20,120 120,20 Z"
            fill="url(#sheen-back)" stroke="#c9a227" stroke-width="5"/>
    </svg>
    <div class="label-content">
      <div class="origin">Atlanta's<br>Local Honey</div>
      <div class="origin-counties">Bees kept in Cobb, Cherokee, DeKalb, Douglas, Forsyth, Gwinnett, Hall &amp; Jackson Counties.</div>
      <h2 class="section-title">Sustainable Beekeeping</h2>
      <div class="story">
        <p>* Partnering with local farmers and landowners we spread our bees out over many square miles, keeping fewer bees at more locations. Although much more time consuming and expensive, it allows the pollinators to benefit more of the environment and ensures them more abundant natural food. This eliminates the need to feed cane sugar or high fructose corn syrups which results in healthier bees and purer honey, not contaminated with syrup.</p>
        <p>* We will never sacrifice the health of the bees or the quality of their honey for profit. Never!</p>
        <p>* We sell honey from our bees only.</p>
        <p>* Do not feed to infants under 1 year old.</p>
      </div>
      <div class="web">http://lin-Wrens.com</div>
      <div class="nutrition">
        <div class="nutrition-title">Nutrition Facts</div>
        Serv. Size 1 Tbsp (21g) / Serv. Per Container 21<br>
        Percent Daily Values (DV)<br>are based on a 2,000 calorie diet.<br>
        Amount Per Serving
        <table>
          <tr><td>Calories</td><td>64</td><td></td></tr>
          <tr><td>Total Fat</td><td>0g</td><td>0% DV</td></tr>
          <tr><td>Sodium</td><td>0mg</td><td>0% DV</td></tr>
          <tr><td>Total Carbs</td><td>17g</td><td>6% DV</td></tr>
          <tr><td>Sugars</td><td>16g</td><td></td></tr>
          <tr><td>Protein</td><td>0g</td><td>0% DV</td></tr>
        </table>
      </div>
      <div class="bee-mark" role="img" aria-label="Small honeybee illustration"></div>
    </div>
  </section>

</main>
</body>
</html>
```